Vantor Marketing eCommerce (a-la-carte) Modern Edgy (Be Creative - Follow Brief)

//VANTOR MARKETING//
A-La-Carte style eCommerce site designed with pick and pay options. Full credit card payment gateway. Paypal offered, Google Pay, Apple Pay. (Open to suggestions: Wordpress, BigCommerce, Squarespace)

Designed to fit look and feel of logo. Warm, Inviting, Simple and Modern.

Pages (standard 5):
1. Main Page: Sample Cases/Photos, Hot Packages
2. About: Company statement, Staff bios, Our goals
3. Services: Place to list options, service offerings, prices of packages (ability to check out, pay, etc)
4. Portfolio: Place to showcase our work, testimonials, ratings
5. Contact: Contact form, Links to other platforms (Whatsapp, Telegram, Discord)

Links to Social Media, include ability to share throughout whole page.

***(See attached Logo - use for look and feel but feel free to be creative, only a suggestion)***

Target Market(s)

Business, Influencers, Brands

Industry/Entity Type

Branding & Marketing

Coding

Coded - Design and coding required

Number of Pages Required

5+ page

Colors
0054AA
0677BA
7BADD7
CADEEF
E8F1F8

Requirements
Must have
• Must be clean, easy to navigate, modern look and feel but warm and inviting
Nice to have
• Front Page - Main "HOT" offerings // About Page // Contact Page (Form - Links to Whatsapp, Telegram, Discord) // Services // Portfolio page -- Social Media Links
Should not have
• clutter.

```html
<!DOCTYPE html>
<html lang="en">
<head>
<meta charset="utf-8">
<title>Vantor Marketing</title>
<link rel="stylesheet" href="https://fonts.googleapis.com/css2?family=Dancing+Script:wght@700&family=Roboto:wght@400;500;700&display=swap">
<style>
:root{
  --teal:#2a93b8;
  --ink:#111111;
  --text:#444444;
  --white:#ffffff;
  --dark:#1b1b1d;
  --soft:#f3f3f3;
}
*{margin:0;padding:0;box-sizing:border-box}
html,body{width:1200px;height:3559px;overflow:hidden;background:var(--white)}
body{position:relative;font-family:"Roboto",sans-serif;color:var(--text)}
.abs{position:absolute}
.script{font-family:"Dancing Script",cursive;font-weight:700;color:var(--ink)}
.btn{position:absolute;display:flex;align-items:center;justify-content:center;border-radius:22px;background:var(--teal);color:var(--white);font-size:15px}

/* header */
.topbar{left:380px;top:0;width:820px;height:51px;background:var(--ink);border-radius:0 0 0 26px;color:var(--white);font-size:13.5px;display:flex;align-items:center;gap:26px;padding-left:48px}
.topbar span{display:flex;align-items:center;gap:10px}
.brand{display:flex;align-items:center;gap:10px;font-size:20px;font-weight:500;color:var(--ink)}
.brand i{display:block;width:22px;height:22px;border-radius:50%;background:var(--teal)}
.nav{left:428px;top:82px;display:flex;gap:34px;font-size:16px;color:var(--ink)}

/* hero */
.hero{left:0;top:131px;width:1200px;height:601px;background:linear-gradient(90deg,#0b0d12 0%,#111823 40%,#1d3a5c 65%,#25507d 85%,#1a2f4c 100%)}
.hero-photo{left:600px;top:0;width:600px;height:601px;background:radial-gradient(circle at 45% 60%,rgba(110,200,255,.55),rgba(40,110,180,.25) 35%,transparent 65%)}
.hero h1{left:110px;top:92px;font-size:84px;line-height:98px;color:var(--white)}
.hero p{left:110px;top:313px;width:600px;font-size:25px;line-height:35px;color:var(--white)}
.hero .pill{left:113px;top:457px;width:171px;height:42px;background:var(--white);color:var(--ink);border-radius:22px;display:flex;align-items:center;justify-content:center;font-size:15px}
.dots{display:flex;gap:9px;align-items:center}
.dots b{display:block;width:9px;height:9px;border-radius:50%;background:#c9c9c9}

/* about */
.about-title{left:112px;top:830px;font-size:44px}
.about-text{left:112px;top:912px;width:385px;font-size:15.5px;line-height:26px}
.about-text p+p{margin-top:24px}
.about-photo{left:552px;top:818px;width:536px;height:459px;background:linear-gradient(135deg,#1e3a5c,#d9e2ea 45%,#eef2f5 70%,#3aa6c9)}

/* packages */
.band{left:0;top:1364px;width:1200px;height:404px;background:linear-gradient(90deg,#1a1a1c,#2a2a2d 50%,#1a1a1c)}
.pk-title{left:0;top:1428px;width:1200px;text-align:center;font-size:44px;color:var(--white)}
.pk-intro{left:190px;top:1506px;width:820px;text-align:center;color:var(--white);font-size:15.5px;line-height:26px}
.card{top:1649px;width:283px;height:336px;background:var(--white);box-shadow:0 4px 14px rgba(0,0,0,.15);text-align:center}
.card svg{margin-top:28px}
.card h3{margin-top:8px;font-size:20px;font-weight:700;color:var(--ink)}
.card p{margin:14px auto 0;width:210px;font-size:15px;line-height:22px;color:#666}
.card .price{margin-top:14px;font-size:25px;font-weight:500;color:var(--ink)}
.card .btn{left:56px;top:262px;width:171px;height:42px}

/* services */
.sec-title{font-size:44px}
.arrow{width:32px;height:32px;border-radius:50%;background:var(--teal);display:flex;align-items:center;justify-content:center}
.svc{top:2158px;width:299px}
.svc .ph{height:260px}
.svc h4{margin-top:24px;font-size:20px;font-weight:500;color:var(--teal)}
.svc p{margin-top:14px;font-size:16px;line-height:26px;color:#333}
.port{top:2744px;width:305px;height:304px;border-radius:4px}

/* footer */
.footer{left:0;top:3179px;width:1200px;height:380px;background:#000;color:var(--white)}
.footer h5{font-size:20px;font-weight:700}
.footer ul{list-style:none;font-size:15.5px;line-height:26px}
.social{display:flex;gap:21px}
.social i{display:block;width:22px;height:22px;border:2px solid var(--white);border-radius:3px}
.rule{left:112px;top:331px;width:976px;height:1px;background:#888}
</style>
</head>
<body>

<header>
  <div class="abs topbar">
    <span>Monday - Friday: 9am - 5pm Saturday - Sunday: Closed</span>
    <span><svg width="18" height="18" viewBox="0 0 24 24" fill="none" stroke="#fff" stroke-width="2"><path d="M5 3h4l2 5-3 2a11 11 0 0 0 6 6l2-3 5 2v4a2 2 0 0 1-2 2A17 17 0 0 1 3 5a2 2 0 0 1 2-2z"/></svg>+ 1 555-010-2040</span>
    <span><svg width="22" height="16" viewBox="0 0 22 16" fill="none" stroke="#fff" stroke-width="1.8"><rect x="1" y="1" width="20" height="14"/><path d="M1 1l10 8 10-8"/></svg>info@kelvora.com</span>
  </div>
  <div class="abs brand" style="left:112px;top:54px"><i></i>Vantor Marketing</div>
  <nav class="abs nav"><span>Home</span><span>About</span><span>Services</span><span>Portfolio</span><span>Contact</span></nav>
  <svg class="abs" style="left:866px;top:79px" width="24" height="24" viewBox="0 0 24 24" fill="none" stroke="#111" stroke-width="2"><circle cx="10" cy="10" r="7"/><path d="M15 15l7 7"/></svg>
  <div class="btn" style="left:917px;top:69px;width:171px;height:43px;font-size:17px;font-weight:500">Get Started</div>
</header>

<section class="abs hero">
  <div class="abs hero-photo" role="img" aria-label="Hand holding a glowing rising bar chart with arrows in front of a businessman in a suit"></div>
  <h1 class="abs script">Welcome to<br>Vantor Marketing</h1>
  <p class="abs">Lorem ipsum dolor sit amet, consectetur adipiscing elit, sed do eiusmod tempor incididunt ut labore et dolore magna aliqua.</p>
  <div class="abs pill">Contact Us</div>
  <div class="abs dots" style="left:561px;top:536px"><b style="width:22px;height:22px;background:#fff"></b><b></b><b></b><b></b></div>
</section>

<section>
  <h2 class="abs script about-title">About Us</h2>
  <div class="abs about-text">
    <p>Lorem ipsum dolor sit amet, consectetur adipiscing elit, sed do eiusmod tempor incididunt ut labore et dolore magna aliqua. Ut enim ad minim veniam, quis nostrud exercitation ullamco laboris nisi ut aliquip ex ea commodo consequat.</p>
    <p>Duis aute irure dolor in reprehenderit in voluptate velit esse cillum dolore eu fugiat nulla pariatur. Excepteur sint occaecat cupidatat non proident, sunt in culpa qui officia deserunt mollit anim id est laborum.</p>
  </div>
  <div class="btn" style="left:112px;top:1210px;width:171px;height:42px">Read More</div>
  <div class="abs about-photo" role="img" aria-label="Two colleagues reviewing printed charts and reports on a desk with a calculator"></div>
</section>

<section>
  <div class="abs band" role="img" aria-label="Dark blurred background of a business meeting"></div>
  <h2 class="abs script pk-title">Hot Packages</h2>
  <p class="abs pk-intro">Nemo enim ipsam voluptatem quia voluptas sit aspernatur aut odit aut fugit, sed quia consequuntur magni dolores eos qui ratione voluptatem sequi nesciunt. Neque porro quisquam est, qui dolorem ipsum quia dolor sit amet, consectetur, adipisci velit, sed quia non numquam eius modi tempora incidunt ut labore et dolore magnam aliquam quaerat voluptatem.</p>

  <div class="abs card" style="left:112px">
    <svg width="56" height="46" viewBox="0 0 56 46" fill="none" stroke="#2a93b8" stroke-width="2"><path d="M2 10l10-6 8 4 8-2 8 2 8-4 10 6"/><path d="M12 4l-6 20 14 14 6-4 6 4 14-14-6-20"/><path d="M20 22l6 6M26 20l6 6M32 18l6 6"/></svg>
    <h3>Basic</h3>
    <p>Excepteur sint occaecat non proident, sunt in culpa qui deserunt mollit laborum.</p>
    <div class="price">$ 30/mo</div>
    <div class="btn">Buy Now</div>
  </div>
  <div class="abs card" style="left:458px">
    <svg width="48" height="60" viewBox="0 0 48 60" fill="none" stroke="#2a93b8" stroke-width="2"><circle cx="24" cy="22" r="20"/><circle cx="24" cy="22" r="13"/><path d="M17 22l5 5 9-10"/><path d="M14 40l-6 16 8-3 4 6 4-10M34 40l6 16-8-3-4 6-4-10"/></svg>
    <h3>Standard</h3>
    <p>Excepteur sint occaecat non proident, sunt in culpa qui deserunt mollit laborum.</p>
    <div class="price">$ 50/mo</div>
    <div class="btn">Buy Now</div>
  </div>
  <div class="abs card" style="left:805px">
    <svg width="54" height="54" viewBox="0 0 54 54" fill="none" stroke="#2a93b8" stroke-width="2"><path d="M16 22l-2-16 7 7 6-9 6 9 7-7-2 16z"/><path d="M16 27h22"/><path d="M4 38h14l8 4h10l12-8v10l-14 8H14l-10-4z"/></svg>
    <h3>Premium</h3>
    <p>Excepteur sint occaecat non proident, sunt in culpa qui deserunt mollit laborum.</p>
    <div class="price">$ 60/mo</div>
    <div class="btn">Buy Now</div>
  </div>
</section>

<section>
  <h2 class="abs script sec-title" style="left:112px;top:2060px">Our Services</h2>
  <div class="abs arrow" style="left:1012px;top:2073px"><svg width="12" height="14" viewBox="0 0 12 14" fill="none" stroke="#fff" stroke-width="2.4"><path d="M8 2L3 7l5 5"/></svg></div>
  <div class="abs arrow" style="left:1057px;top:2073px"><svg width="12" height="14" viewBox="0 0 12 14" fill="none" stroke="#fff" stroke-width="2.4"><path d="M4 2l5 5-5 5"/></svg></div>

  <div class="abs svc" style="left:112px">
    <div class="ph" role="img" aria-label="Hand touching a tablet with glowing financial charts" style="background:linear-gradient(135deg,#4cc2ef,#1b4f8c 60%,#0f2f5c)"></div>
    <h4>Lorem ipsum dolor sit</h4>
    <p>Ut enim ad minim veniam, quis nostrud exercitation Ut enim commodo consequat.</p>
  </div>
  <div class="abs svc" style="left:450px">
    <div class="ph" role="img" aria-label="Man working on a laptop showing charts" style="background:linear-gradient(135deg,#e9e9e9,#8a9aa8 55%,#4b6a8a)"></div>
    <h4>Sed ut perspiciatis unde</h4>
    <p>Ut enim ad minim veniam, quis nostrud exercitation Ut enim commodo consequat.</p>
  </div>
  <div class="abs svc" style="left:788px">
    <div class="ph" role="img" aria-label="Team meeting in a bright office with a presenter at a whiteboard" style="background:linear-gradient(135deg,#f2f2f2,#c9c6c0 55%,#8c7a66)"></div>
    <h4>Finibus Bonorum et</h4>
    <p>Ut enim ad minim veniam, quis nostrud exercitation Ut enim commodo consequat.</p>
  </div>
</section>

<section>
  <h2 class="abs script sec-title" style="left:0;top:2628px;width:1200px;text-align:center">Our Portfolio</h2>
  <div class="abs port" style="left:112px;background:linear-gradient(135deg,#d8d8d6,#9a8f80 55%,#5d5a55)" role="img" aria-label="Colleagues working together on laptops at a shared desk"></div>
  <div class="abs port" style="left:447px;background:linear-gradient(135deg,#efefec,#c2bfb8 50%,#7d6a5a)" role="img" aria-label="Open coworking space with people talking and working"></div>
  <div class="abs port" style="left:783px;background:linear-gradient(135deg,#d6cfc6,#8f7864 55%,#4b5d6e)" role="img" aria-label="Smiling man working at a computer in an office"></div>
  <div class="abs dots" style="left:570px;top:3079px;gap:14px"><b></b><b style="width:13px;height:13px;background:var(--teal)"></b><b></b></div>
</section>

<footer class="abs footer">
  <div class="abs brand" style="left:112px;top:80px;color:#fff;font-size:24px"><i style="width:28px;height:28px"></i>Vantor Marketing</div>
  <div class="abs social" style="left:112px;top:249px"><i></i><i></i><i></i></div>
  <div class="abs" style="left:552px;top:68px">
    <h5>Links</h5>
    <ul style="margin-top:12px"><li>Home</li><li>About</li><li>Services</li><li>Portfolio</li><li>Contact</li></ul>
  </div>
  <div class="abs" style="left:858px;top:68px">
    <h5>Contact Us</h5>
    <ul style="margin-top:12px;line-height:36px"><li>123, Vantor Marketing ,na 123456.</li><li>Info@ Vantor Marketing.com</li><li>+ 1 555-010-2040</li></ul>
  </div>
  <div class="abs rule"></div>
  <div class="abs" style="left:112px;top:345px;font-size:13.5px">Copyright © 2023 Vantor Marketing.All Rights Reserved.</div>
</footer>

</body>
</html>
```